Wordpress Design Project

NOTICE TO DESIGNERS
****************NOTE: PLEASE DO NOT SUBMIT ANY MORE DESIGNS, THANK YOU!!!!****************
The name of our business is Handset Lab Crew and we are setting up a website to review new phones/tablets in the marketplace.
We require a 5 page design, the idea behind the project can be understood better if you visit this websites
1) dorvanix.com
2) http://plrv.com/reviews/cellphones/
Pages required are;
1) Home page which lists all the current top devices
2) A single device page that shows the device with its current specs
3) Comparison page - where 2 or 3 devices are being compared in terms of specs
4) Archive page that shows all the current videos and text reviews
5) Single post page for the device being reviewed with all its pictures, written review, video with sidebar on the side showing other reviews available.
I am opened to a nice color scheme, including red, blue and orange. We do not have any logo at the moment. Thanks
Updates
This is a notice to all designers, I have found the designer I want to work with please do not submit any more designs for now. Thank you

```html
<!DOCTYPE html>
<html lang="en">
<head>
<meta charset="utf-8">
<title>Handset Lab Crew</title>
<link rel="stylesheet" href="https://fonts.googleapis.com/css2?family=Montserrat:wght@500;600;700&family=Open+Sans:wght@400;600;700&family=Arimo:wght@400&display=swap">
<style>
  :root {
    --accent: #ffba00;
    --ink: #141414;
    --ink-soft: #444444;
    --muted: #9a9a9a;
    --paper: #ffffff;
    --rule: #dddddd;
    --tab-dark: #3a3a3a;
    --caption-bg: #151515;
    --backdrop-a: #1a1a1a;
    --backdrop-b: #4a4a4a;
    --hero-a: #f1f1f1;
    --hero-b: #d4d4d4;
  }
  * { box-sizing: border-box; margin: 0; padding: 0; }
  html, body { width: 1200px; height: 603px; overflow: hidden; }
  body {
    position: relative;
    font-family: "Open Sans", Arial, sans-serif;
    background: var(--backdrop-a);
  }
  .backdrop {
    position: absolute; inset: 0;
    background: linear-gradient(160deg, var(--backdrop-a) 0%, var(--backdrop-b) 45%, var(--backdrop-a) 100%);
  }
  .page {
    position: absolute; left: 85px; top: 0; width: 1030px; height: 603px;
    background: var(--paper);
  }
  .brand {
    position: absolute; left: 40px; top: 40px;
    font-family: "Montserrat", sans-serif; font-weight: 600;
    color: var(--ink); text-transform: uppercase;
    font-size: 44px; line-height: 42px; letter-spacing: 0.5px;
  }
  .ad-slot {
    position: absolute; left: 522px; top: 52px; width: 468px; height: 60px;
    border: 1px solid var(--rule);
    display: flex; align-items: center; justify-content: center;
    font-family: "Open Sans", sans-serif; font-size: 14px; color: var(--muted); letter-spacing: 1px;
  }
  .main-nav {
    position: absolute; left: 40px; top: 153px; height: 32px;
    font-family: "Montserrat", sans-serif; font-weight: 600; font-size: 14.5px;
    text-transform: uppercase; color: var(--ink-soft);
  }
  .main-nav a {
    position: absolute; top: 0; height: 32px; line-height: 33px;
    color: inherit; text-decoration: none; white-space: nowrap;
  }
  .main-nav .is-active {
    left: 0; width: 99px; text-align: center;
    background: var(--accent); color: var(--paper);
  }
  .main-nav .search svg { vertical-align: -1px; margin-left: 4px; }
  .hero {
    position: absolute; left: 39px; top: 222px; width: 624px; height: 355px;
  }
  .hero-image {
    position: absolute; inset: 0;
    background: linear-gradient(150deg, var(--hero-a) 0%, #e6e6e6 55%, var(--hero-b) 100%);
  }
  .hero-caption {
    position: absolute; left: 0; right: 0; bottom: 0; height: 93px;
    background: var(--caption-bg); color: var(--paper);
    padding: 18px 23px 0;
  }
  .hero-caption h2 {
    font-family: "Montserrat", sans-serif; font-weight: 700; font-size: 14.5px;
    letter-spacing: 0.3px; line-height: 18px;
  }
  .hero-caption p {
    font-family: "Arimo", Arial, sans-serif; font-size: 14px; line-height: 18px;
    text-transform: uppercase;
  }
  .sidebar { position: absolute; left: 685px; top: 222px; width: 286px; }
  .tabs { display: flex; height: 31px; }
  .tabs span {
    width: 95px; text-align: center; line-height: 31px;
    font-size: 14px; color: var(--paper); background: var(--tab-dark);
  }
  .tabs .is-active { background: var(--accent); }
  .post-list { list-style: none; position: absolute; top: 55px; left: 0; }
  .post {
    position: relative; height: 84px; width: 286px;
  }
  .post-thumb {
    position: absolute; left: 0; top: 0; width: 51px; height: 50px;
    background: var(--accent);
  }
  .post-title {
    position: absolute; left: 66px; top: 1px; width: 190px;
    font-size: 12px; line-height: 12.5px; color: var(--ink-soft); text-transform: uppercase;
  }
  .post-title strong { font-weight: 700; }
  .post-views {
    position: absolute; left: 66px; top: 35px;
    font-size: 8.5px; font-weight: 700; color: var(--ink);
  }
</style>
</head>
<body>
  <div class="backdrop" role="img" aria-label="Dark monochrome architectural photo backdrop"></div>

  <div class="page">
    <div class="brand">Handset Lab<br>Crew</div>

    <div class="ad-slot">468 X 60</div>

    <nav class="main-nav">
      <a class="is-active" href="#">Home</a>
      <a style="left:134px" href="#">Phones</a>
      <a style="left:242px" href="#">More Phones</a>
      <a style="left:386px" href="#">And Even More</a>
      <a class="search" style="left:626px" href="#">Search<svg width="16" height="10" viewBox="0 0 16 10"><path d="M0 5h14M10 1l4 4-4 4" fill="none" stroke="currentColor" stroke-width="1.8"/></svg></a>
    </nav>

    <section class="hero">
      <div class="hero-image" role="img" aria-label="Light grey photo of paper sketches showing phone wireframes"></div>
      <div class="hero-caption">
        <h2>MOBILE REVIEWS AND COMPARISONS</h2>
        <p>Lorem ipsum dolor sit amet, consectetuer adipiscing elit, sed diam<br>nonummy nibh euismod tincidunt ut laoreet dolore magna aliquam.</p>
      </div>
    </section>

    <aside class="sidebar">
      <div class="tabs">
        <span class="is-active">Popular</span>
        <span>Latest</span>
        <span>Fans</span>
      </div>
      <ul class="post-list">
        <li class="post"><div class="post-thumb"></div><p class="post-title"><strong>Novafone5 -</strong> Read the latest in-depth review.</p><p class="post-views">38295 view(s)</p></li>
        <li class="post"><div class="post-thumb"></div><p class="post-title"><strong>Novafone5 -</strong> Read the latest in-depth review.</p><p class="post-views">38295 view(s)</p></li>
        <li class="post"><div class="post-thumb"></div><p class="post-title"><strong>Novafone5 -</strong> Read the latest in-depth review.</p><p class="post-views">38295 view(s)</p></li>
        <li class="post"><div class="post-thumb"></div><p class="post-title"><strong>Novafone5 -</strong> Read the latest in-depth review.</p><p class="post-views">38295 view(s)</p></li>
      </ul>
    </aside>
  </div>
</body>
</html>
```